RT Pemberly Electric Yard Sign

Looking to have a yard sign designed that we can place at projects we are working on. Most likely will be 18" H x 24" W but flexible that we can increase the size if necessary. It should include our logo, our phone # 609-555-0147, website rtpemberlyelectric-example.com and slogan, built on integrity, driven by excellence. Colors should match our brand.

```html
<!DOCTYPE html>
<html lang="en">
<head>
<meta charset="utf-8">
<title>RT Pemberly Electric Yard Sign</title>
<link rel="stylesheet" href="https://fonts.googleapis.com/css2?family=Anton&family=Montserrat:wght@800&family=Oswald:wght@600&display=swap">
<style>
  :root {
    --navy: #001f3f;
    --red: #e41e26;
    --white: #ffffff;
    --backdrop: #e9ebee;
  }
  * { margin: 0; padding: 0; box-sizing: border-box; }
  html, body { width: 1200px; height: 1200px; overflow: hidden; background: var(--backdrop); }
  .yard-sign {
    position: absolute; left: 180px; top: 40px;
    width: 840px; height: 1120px;
    background: var(--white);
    overflow: hidden;
    box-shadow: 0 8px 30px rgba(0,0,0,.18);
  }
  .sign-shapes { position: absolute; inset: 0; }
  .brand-name {
    position: absolute; left: 0; right: 0; top: 225px;
    display: flex; align-items: center; justify-content: center; gap: 20px;
    font-family: "Montserrat", sans-serif; font-weight: 800;
    font-size: 54px; color: var(--navy); letter-spacing: 1px;
  }
  .brand-mark { width: 30px; height: 30px; background: var(--red); }
  .slogan {
    position: absolute; left: 0; right: 0; top: 540px;
    text-align: center;
    font-family: "Anton", sans-serif; font-size: 96px; line-height: 100px;
    color: var(--white); text-transform: uppercase; letter-spacing: 1px;
    text-shadow: 4px 4px 0 #000c1a;
  }
  .phone {
    position: absolute; left: 0; right: 0; top: 920px;
    text-align: center;
    font-family: "Montserrat", sans-serif; font-weight: 800;
    font-size: 92px; color: var(--white); letter-spacing: -1px;
  }
  .website {
    position: absolute; left: 0; right: 0; top: 1025px;
    display: flex; align-items: center; justify-content: center; gap: 14px;
    font-family: "Oswald", sans-serif; font-weight: 600;
    font-size: 38px; color: var(--white); letter-spacing: 1px; text-transform: uppercase;
  }
  .website-rule { width: 60px; height: 3px; background: var(--white); }
</style>
</head>
<body>
  <div class="yard-sign">
    <svg class="sign-shapes" width="840" height="1120" viewBox="0 0 840 1120">
      <path d="M0 470 Q420 390 840 470 L840 448 Q420 378 0 448 Z" fill="var(--red)"/>
      <path d="M0 492 Q420 412 840 492 L840 930 L0 930 Z" fill="var(--navy)"/>
      <rect x="0" y="925" width="840" height="195" fill="var(--red)"/>
    </svg>
    <div class="brand-name"><span class="brand-mark"></span>RT Pemberly Electric</div>
    <p class="slogan">Built on integrity,<br>driven by<br>excellence</p>
    <p class="phone">609-555-0147</p>
    <p class="website"><span class="website-rule"></span>rtpemberlyelectric-example.com<span class="website-rule"></span></p>
  </div>
</body>
</html>
```